Need a Brochure Design

We need a brochure designed (A4 two sides or A3 foldable which is equal to 2 x A4 = total of four pages )

Brief and Logo attached.

```html
<!DOCTYPE html>
<html lang="en">
<head>
<meta charset="utf-8">
<title>Home Staging Brochure – Works &amp; Pricing</title>
<link rel="stylesheet" href="https://fonts.googleapis.com/css2?family=Jost:wght@400;500;600;700&family=Crimson+Text:wght@400&family=Bodoni+Moda:opsz,wght@6..96,500&display=swap">
<style>
  :root{
    --ink:#0d0d0d;
    --paper:#ffffff;
    --peach:#fce3cf;
    --red:#d4202a;
    --grey-text:#7a7a7a;
    --burlap-dark:#5e5e5e;
    --burlap-light:#a9a9a9;
    --photo-living:#cfc6b8;
    --photo-kitchen:#b9b3a8;
    --photo-bedroom:#d9d2c2;
    --photo-lounge:#c8c3bb;
  }
  *{margin:0;padding:0;box-sizing:border-box}
  html,body{width:848px;height:1200px;overflow:hidden;background:var(--paper)}
  .page{position:relative;width:848px;height:1200px;background:var(--paper);color:var(--ink);font-family:"Crimson Text",Georgia,serif}

  /* Works section */
  .works-title{position:absolute;left:51px;top:50px;font-family:"Jost",sans-serif;font-weight:600;font-size:35px;letter-spacing:.2px}
  .photo{position:absolute}
  .photo--living{left:51px;top:107px;width:266px;height:177px;background:linear-gradient(160deg,#ecebe8 0%,var(--photo-living) 60%,#a8885f 100%)}
  .photo--kitchen{left:324px;top:107px;width:140px;height:177px;background:linear-gradient(180deg,#f1f0ec 0%,var(--photo-kitchen) 55%,#7c7a74 100%)}
  .photo--bedroom{left:51px;top:292px;width:146px;height:194px;background:linear-gradient(180deg,#eeeae3 0%,var(--photo-bedroom) 55%,#b7b3ad 100%)}
  .photo--lounge{left:203px;top:292px;width:261px;height:194px;background:linear-gradient(180deg,#e9e7e2 0%,var(--photo-lounge) 60%,#a8a29a 100%)}

  .divider{position:absolute;left:498px;top:52px;width:3px;height:434px;background:var(--ink)}

  .stats{position:absolute;left:532px;top:51px;width:266px;height:141px}
  .stat-text{position:absolute;text-align:center;width:120px;line-height:1}
  .stat-small{font-size:14px}
  .stat-big{font-family:"Jost",sans-serif;font-weight:600;font-size:34px;line-height:1.05}
  .stat--projects{left:10px;top:27px}
  .stat--days{left:134px;top:25px}
  .stat--days .stat-small{display:block;line-height:1.2}

  .benefits{position:absolute;left:533px;top:204px;width:270px;list-style:none}
  .benefits li{position:relative;padding-left:26px;font-size:14px;line-height:17px;margin-bottom:8px}
  .benefits li::before{content:"";position:absolute;left:2px;top:9px;width:3px;height:3px;border-radius:50%;background:var(--ink)}
  .tagline{position:absolute;left:533px;top:416px;width:230px;font-size:14px;line-height:17px;color:var(--red)}

  /* Pricing section */
  .burlap{position:absolute;left:0;top:521px;width:848px;height:679px;background:radial-gradient(circle at 30% 40%,var(--burlap-light) 0%,#8a8a8a 50%,var(--burlap-dark) 100%)}
  .price-panel{position:absolute;left:52px;top:571px;width:745px;height:577px;background:var(--paper)}
  .price-title{position:absolute;left:0;top:590px;width:848px;text-align:center;font-family:"Jost",sans-serif;font-weight:400;font-size:64px;line-height:1}
  .price-subtitle{position:absolute;left:0;top:664px;width:848px;text-align:center;font-family:"Jost",sans-serif;font-weight:600;font-size:44px;line-height:1}

  .grid-v{position:absolute;left:420px;top:747px;width:3px;height:298px;background:var(--ink)}
  .grid-h{position:absolute;left:119px;width:613px;height:3px;background:var(--ink)}
  .grid-h--mid{top:891px}
  .grid-h--end{top:1068px}

  .plan{position:absolute}
  .plan-number{position:absolute;font-family:"Bodoni Moda",Didot,serif;font-weight:500;font-size:158px;line-height:1;top:-20px}
  .plan-label{position:absolute;font-family:"Jost",sans-serif;font-weight:600;font-size:30px;line-height:33px;white-space:nowrap}
  .plan-price{position:absolute;font-size:15.5px;line-height:17px;color:var(--red);white-space:nowrap}
  .plan-price s{display:block;color:var(--grey-text);font-size:13.5px}

  .plan--one{left:0;top:748px}
  .plan--one .plan-number{left:124px}
  .plan--one .plan-label{left:198px;top:0}
  .plan--one .plan-price{left:214px;top:81px}

  .plan--two{left:0;top:748px}
  .plan--two .plan-number{left:452px}
  .plan--two .plan-label{left:554px;top:0}
  .plan--two .plan-price{left:561px;top:81px}

  .plan--three{left:0;top:928px}
  .plan--three .plan-number{left:126px}
  .plan--three .plan-label{left:221px;top:0}
  .plan--three .plan-price{left:235px;top:82px}

  .plan--four{left:0;top:928px}
  .plan--four .plan-number{left:451px}
  .plan--four .plan-label{left:550px;top:0}
  .plan--four .plan-price{left:567px;top:82px}

  .footnote{position:absolute;left:127px;top:1078px;width:300px;font-size:13.5px;line-height:17px}
</style>
</head>
<body>
<div class="page">
  <h1 class="works-title">Our Works</h1>
  <div class="photo photo--living" role="img" aria-label="Photo of a staged open-plan living room with sofa, coffee tables and timber floor"></div>
  <div class="photo photo--kitchen" role="img" aria-label="Photo of a styled kitchen with pendant lights and cushions on a sofa"></div>
  <div class="photo photo--bedroom" role="img" aria-label="Photo of a staged bedroom with cloud artwork and cushions"></div>
  <div class="photo photo--lounge" role="img" aria-label="Photo of a staged lounge with two grey sofas, patterned rug and large windows"></div>

  <div class="divider"></div>

  <div class="stats">
    <svg width="266" height="141" viewBox="0 0 266 141" aria-hidden="true">
      <circle cx="70" cy="70" r="68" fill="var(--peach)" stroke="var(--ink)" stroke-width="2"/>
      <circle cx="194" cy="70" r="68" fill="var(--peach)" stroke="var(--ink)" stroke-width="2"/>
    </svg>
    <div class="stat-text stat--projects">
      <div class="stat-small">over</div>
      <div class="stat-big">185</div>
      <div class="stat-small">projects/year</div>
    </div>
    <div class="stat-text stat--days">
      <span class="stat-small">selling in</span>
      <span class="stat-small">less than</span>
      <div class="stat-big" style="margin-top:6px">30</div>
      <div class="stat-small">days</div>
    </div>
  </div>

  <ul class="benefits">
    <li>Helping your property reach its highest potential without busting the budget.</li>
    <li>Achieving a record number of viewings and the highest possible sale price.</li>
    <li>Installation, interior design and decoration, and removal included.</li>
    <li>Pre-sale home preparation to post-sale removal.</li>
    <li>Free consultation and longer rental periods.</li>
  </ul>
  <p class="tagline">A small investment for such a large transformation!</p>

  <div class="burlap" role="img" aria-label="Grey woven burlap texture background"></div>
  <div class="price-panel"></div>

  <h2 class="price-title">Our Price Tables</h2>
  <p class="price-subtitle">Full Styling + 6 Weeks Free Hire*</p>

  <div class="grid-v"></div>
  <div class="grid-h grid-h--mid"></div>
  <div class="grid-h grid-h--end"></div>

  <div class="plan plan--one">
    <span class="plan-number">1</span>
    <span class="plan-label">Bedroom<br>Property</span>
    <p class="plan-price">$ 1,897.00 AUD<s>$ 2,750.00 AUD</s></p>
  </div>
  <div class="plan plan--two">
    <span class="plan-number">2</span>
    <span class="plan-label">Bedroom<br>Property</span>
    <p class="plan-price">$ 2,697.00 AUD<s>$ 3,250.00 AUD</s></p>
  </div>
  <div class="plan plan--three">
    <span class="plan-number">3</span>
    <span class="plan-label">Bedroom<br>Property</span>
    <p class="plan-price">$ 2,997.00 AUD<s>$ 4,470.00 AUD</s></p>
  </div>
  <div class="plan plan--four">
    <span class="plan-number">4</span>
    <span class="plan-label">Bedroom<br>Property</span>
    <p class="plan-price">$ 3,897.00 AUD<s>$ 5,485.00 AUD</s></p>
  </div>

  <p class="footnote">* 4 Weeks Free Hire + 2 Weeks Free Extension (if property not sold within 4 weeks)</p>
</div>
</body>
</html>
```